Calm Summit website development

Need a website designed for a coaching business. Very high-end, luxury, professionalism, in the area of STRESS, see brief attached. I have a logo already
Updates

Slow in providing feedback

Target Market(s)

CEOs very successful men and wealthy females, high end luxury market

Industry/Entity Type

coaching

Number of Pages Required

1 page

Requirements
Must have
• Luxury look, professional, serious but warm, appealing to both sexes

```html
<!DOCTYPE html>
<html lang="en">
<head>
<meta charset="utf-8">
<title>Calm Summit — Head Coach</title>
<link rel="stylesheet" href="https://fonts.googleapis.com/css2?family=Poppins:wght@300;400;500;600;700;800&display=swap">
<style>
:root{
  --ink:#231f20;
  --ink-soft:#555;
  --teal:#1aa3b5;
  --teal-deep:#0e7f96;
  --paper:#ffffff;
  --mist:#f4f5f6;
  --line:#d9d9d9;
  --footer-bottom:#333132;
}
*{box-sizing:border-box;margin:0;padding:0}
html,body{width:1200px;height:3431px;overflow:hidden}
body{position:relative;font-family:'Poppins',sans-serif;color:var(--ink);background:var(--paper)}
.abs{position:absolute}

/* top bar */
.topbar{left:0;top:0;width:1200px;height:41px;background:var(--ink);color:#fff;font-size:12px}
.topbar span{position:absolute;top:12px;display:flex;align-items:center;gap:5px}
.social{display:flex;gap:8px}
.social i{display:block;width:12px;height:12px;border-radius:50%;background:currentColor}

/* nav */
.nav{left:0;top:41px;width:1200px;height:75px;background:#fff}
.brand{position:absolute;left:89px;top:44px;display:flex;align-items:center;gap:8px;font-size:15px;font-weight:600;letter-spacing:4px;color:var(--ink)}
.brand b{display:block;width:14px;height:14px;background:var(--ink)}
.menu{position:absolute;left:666px;top:26px;display:flex;gap:24px;font-size:15px}
.menu a{color:var(--ink);text-decoration:none;position:relative}
.menu a.active{color:var(--teal-deep)}
.menu a.active::after{content:"";position:absolute;left:-3px;right:-3px;top:48px;height:4px;background:var(--teal)}

/* hero */
.hero{left:0;top:116px;width:1200px;height:545px;background:linear-gradient(100deg,#0f9db2 0%,#37b7c6 38%,#a9cfc8 58%,#e3c39a 75%,#c98f5e 100%)}
.hero-title{left:90px;top:240px;color:#fff;line-height:1}
.hero-title .l1{font-size:53px;font-weight:300}
.hero-title .l1 b{font-weight:700}
.hero-title .l2{font-size:80px;font-weight:800;margin-top:4px;margin-left:-4px}
.btn-dark{background:var(--ink);color:#fff;font-size:13px;font-weight:600;display:flex;align-items:center;justify-content:center;gap:6px}
.hero-btn{left:95px;top:413px;width:199px;height:39px}
.badge{left:570px;top:620px;width:60px;height:60px;border-radius:50%;background:#fff;box-shadow:0 4px 14px rgba(0,0,0,.15)}

/* welcome */
.blob{left:102px;top:733px;width:490px;height:500px;border-radius:48% 52% 45% 55%/55% 45% 55% 45%;background:linear-gradient(160deg,#8ed3dd,#3fb0c1 45%,#a8b9ee);transform:rotate(-12deg)}
.portrait{left:127px;top:740px;width:466px;height:466px;border-radius:50%;background:linear-gradient(135deg,#e9eef1,#c9d6dd 55%,#f1e6d8);box-shadow:0 20px 50px rgba(0,0,0,.15)}
.welcome{left:681px;top:855px;width:400px}
.eyebrow{font-size:21px;font-weight:700;letter-spacing:6px}
.welcome h2{font-size:43px;font-weight:700;line-height:1.1;margin-top:2px}
.welcome h2 span{color:var(--teal)}
.welcome p{font-size:13px;line-height:19.5px;color:var(--ink-soft);margin-top:20px;width:386px}
.link-more{display:inline-block;margin-top:26px;font-size:13px;font-weight:600;padding-bottom:6px;border-bottom:4px solid var(--ink)}

/* why me */
.why-photo{left:666px;top:1319px;width:534px;height:461px;background:linear-gradient(120deg,#f3f3f2,#e6e3dd 50%,#cfc9c0)}
.why-fade{left:300px;top:1319px;width:400px;height:461px;background:linear-gradient(90deg,#fff,rgba(255,255,255,0))}
.why-card{left:90px;top:1416px;width:587px;height:252px;background:#fff;box-shadow:0 6px 30px rgba(0,0,0,.06);padding:24px 22px}
.why-card h2{font-size:45px;font-weight:700;line-height:1}
.why-list{list-style:none;margin-top:24px}
.why-list li{position:relative;padding-left:41px;font-size:14px;line-height:19.5px;color:var(--ink-soft);margin-bottom:21px;width:540px}
.why-list li::before{content:"";position:absolute;left:0;top:2px;width:24px;height:24px;border-radius:50%;background:var(--ink)}

/* benefits */
.benefits-title{left:0;top:1880px;width:1200px;text-align:center}
.benefits-title i{display:block;width:30px;height:30px;margin:0 auto 8px;border-radius:50%;background:var(--ink)}
.benefits-title h2{font-size:45px;font-weight:700;line-height:1.1}
.benefit{width:220px;text-align:center;font-size:18px}
.benefit svg{display:block;margin:0 auto 12px}
.feature{left:384px;top:2178px;width:434px;height:149px;background:#fff;box-shadow:0 6px 30px rgba(0,0,0,.07);text-align:center;padding-top:30px}
.feature-icon{left:570px;top:2142px;width:60px;height:60px;border-radius:50%;background:#fff;box-shadow:0 2px 10px rgba(0,0,0,.12)}
.feature h3{font-size:18px;font-weight:500}
.feature p{font-size:13px;line-height:19.5px;color:var(--ink-soft);width:390px;margin:8px auto 0}

/* appointment */
.dark-band{left:0;top:2775px;width:1200px;height:588px;background:var(--ink)}
.appt-card{left:90px;top:2553px;width:573px;height:478px;background:#fff;box-shadow:0 6px 30px rgba(0,0,0,.08)}
.appt-card h2{position:absolute;left:34px;top:38px;font-size:33px;font-weight:300;letter-spacing:1.5px}
.appt-card h2 b{font-weight:700}
.field{position:absolute;border:1px solid var(--line);background:#fff;font-size:12px;padding:12px 13px;color:#444}
.appt-photo{left:663px;top:2553px;width:449px;height:478px;background:linear-gradient(135deg,#eeeeee,#d9d2c7 45%,#9aa7b8 75%,#c7c0b4)}
.send{position:absolute;left:36px;top:381px;width:180px;height:48px;font-size:16px;letter-spacing:1px}

/* footer */
.footer-brand{left:120px;top:3185px;display:flex;align-items:center;gap:10px;color:#d0d0d0;font-size:20px;font-weight:600;letter-spacing:3px}
.footer-brand b{display:block;width:18px;height:18px;background:#d0d0d0}
.fcol{color:#fff}
.fcol h4{font-size:21px;font-weight:600;margin-bottom:12px}
.fcol p,.fcol li{font-size:12.5px;line-height:20.5px;list-style:none}
.copyright{left:0;top:3363px;width:1200px;height:68px;background:var(--footer-bottom);color:#fff;font-size:13px;text-align:center;padding-top:22px}
</style>
</head>
<body>

<header class="abs topbar">
  <span style="left:88px">
    <svg width="10" height="13" viewBox="0 0 10 13"><path d="M5 0a5 5 0 0 0-5 5c0 3.5 5 8 5 8s5-4.5 5-8a5 5 0 0 0-5-5zm0 7a2 2 0 1 1 0-4 2 2 0 0 1 0 4z" fill="#fff"/></svg>
    Lakeside, TX 70111
  </span>
  <span style="left:231px">
    <svg width="13" height="10" viewBox="0 0 13 10"><rect x=".5" y=".5" width="12" height="9" fill="none" stroke="#fff"/><path d="M.5.5l6 5 6-5" fill="none" stroke="#fff"/></svg>
    hello@calmsummit.example
  </span>
  <span style="left:802px">
    <svg width="12" height="12" viewBox="0 0 12 12"><circle cx="6" cy="6" r="6" fill="#fff"/><path d="M6 2.5V6h2.5" stroke="#231f20" stroke-width="1.4" fill="none"/></svg>
    Office Hours: 8:00 AM - 7:45 PM
  </span>
  <span class="social" style="left:1048px;top:14px"><i></i><i></i><i></i></span>
</header>

<nav class="abs nav">
  <div class="brand"><b></b>CALM SUMMIT</div>
  <div class="menu">
    <a class="active">Home</a><a>About</a><a>Services</a><a>Benefits</a><a>Blog</a><a>Contact Us</a>
  </div>
</nav>

<section>
  <div class="abs hero" role="img" aria-label="Photo of a relaxed woman with glasses, hands behind her head, in warm sunlight over a teal overlay"></div>
  <div class="abs hero-title">
    <div class="l1">HEAD <b>COACH</b></div>
    <div class="l2">GET IT!</div>
  </div>
  <div class="abs btn-dark hero-btn">
    <svg width="12" height="12" viewBox="0 0 12 12"><rect x="1" y="2" width="10" height="9" fill="none" stroke="#fff"/><path d="M1 5h10M4 0v3M8 0v3" stroke="#fff"/></svg>
    Book An Appointment
  </div>
  <div class="abs badge"></div>
</section>

<section>
  <div class="abs blob"></div>
  <div class="abs portrait" role="img" aria-label="Photo of a coach with a clipboard talking with a smiling client"></div>
  <div class="abs welcome">
    <div class="eyebrow">WELCOME TO</div>
    <h2>Calm <span>Summit</span></h2>
    <p>Calm Summit came about due to my desire to help people lead a better and healthier life. Initially, I was involved in the fitness/body side of health. As years passed and my experience grew, I realized how important the mind was in total wellness, and that the mind is all powerful and controlling. Control the mind, control the body and achieve success.</p>
    <a class="link-more">LEARN MORE</a>
  </div>
</section>

<section>
  <div class="abs why-photo" role="img" aria-label="Photo of a smiling coach seated on a sofa holding glasses and a notepad"></div>
  <div class="abs why-fade"></div>
  <div class="abs why-card">
    <h2>Why me?</h2>
    <ul class="why-list">
      <li>Been there done that! Have been through a lot, started businesses, selling a business, law suits, marriage, divorce, second marriage, kids, school, sports, fights, robbed, gun in face, traveled the world, successful, two great kids (both Cadets at Ridgeview Academy...duty/honor/country)</li>
      <li style="width:460px">Limited number of clients...different stage of life, empty nester, have a full career...won't be a number</li>
    </ul>
  </div>
</section>

<section>
  <div class="abs benefits-title"><i></i><h2>Benefits</h2></div>

  <div class="abs benefit" style="left:152px;top:2039px">
    <svg width="100" height="110" viewBox="0 0 100 110"><path d="M50 3l44 25v54L50 107 6 82V28z" fill="var(--ink)"/><circle cx="50" cy="55" r="31" fill="#fff"/><circle cx="50" cy="45" r="7" fill="none" stroke="var(--ink)" stroke-width="2"/><path d="M36 70c2-10 26-10 28 0" fill="none" stroke="var(--ink)" stroke-width="2"/></svg>
    Experience
  </div>
  <div class="abs benefit" style="left:836px;top:2039px">
    <svg width="100" height="110" viewBox="0 0 100 110"><path d="M50 3l44 25v54L50 107 6 82V28z" fill="var(--ink)"/><circle cx="50" cy="55" r="31" fill="#fff"/><path d="M40 48a10 10 0 0 1 20 0c0 8-8 9-8 17a5 5 0 0 1-10 0" fill="none" stroke="var(--ink)" stroke-width="2"/><path d="M64 48a8 8 0 0 1 0 14" fill="none" stroke="var(--ink)" stroke-width="2"/></svg>
    Excellent listener
  </div>
  <div class="abs benefit" style="left:152px;top:2271px">
    <svg width="100" height="110" viewBox="0 0 100 110"><path d="M50 3l44 25v54L50 107 6 82V28z" fill="var(--ink)"/><circle cx="50" cy="55" r="31" fill="#fff"/><circle cx="46" cy="46" r="7" fill="none" stroke="var(--ink)" stroke-width="2"/><path d="M32 70c2-10 20-10 24-6" fill="none" stroke="var(--ink)" stroke-width="2"/><rect x="54" y="60" width="14" height="11" fill="none" stroke="var(--ink)" stroke-width="2"/></svg>
    Private
  </div>
  <div class="abs benefit" style="left:836px;top:2271px">
    <svg width="100" height="110" viewBox="0 0 100 110"><path d="M50 3l44 25v54L50 107 6 82V28z" fill="var(--ink)"/><circle cx="50" cy="55" r="31" fill="#fff"/><g fill="none" stroke="var(--ink)" stroke-width="2"><circle cx="50" cy="55" r="6"/><circle cx="50" cy="55" r="12"/><circle cx="50" cy="55" r="18"/></g></svg>
    Access
  </div>

  <div class="abs feature">
    <h3>Health Wellness</h3>
    <p>Sector expert Health/Wellness. Presented at numerous industry shows and quoted in national publications (not as a coach, I'm new, but in the health &amp; wellness space)</p>
  </div>
  <div class="abs feature-icon">
    <svg width="60" height="60" viewBox="0 0 60 60"><g fill="none" stroke="var(--ink)" stroke-width="1.6"><circle cx="30" cy="30" r="20"/><circle cx="30" cy="22" r="4"/><path d="M22 40c0-8 16-8 16 0M20 36l6-4M40 36l-6-4"/></g></svg>
  </div>
</section>

<section>
  <div class="abs dark-band"></div>
  <form class="abs appt-card">
    <h2>SCHEDULE <b>AN APPOINTMENT</b></h2>
    <div class="field" style="left:36px;top:107px;width:246px;height:41px">First Name</div>
    <div class="field" style="left:294px;top:107px;width:246px;height:41px">Last Name</div>
    <div class="field" style="left:36px;top:163px;width:246px;height:41px">Email</div>
    <div class="field" style="left:294px;top:163px;width:246px;height:41px">Phone Number</div>
    <div class="field" style="left:36px;top:220px;width:504px;height:42px">Type of Service
      <svg style="position:absolute;right:16px;top:17px" width="11" height="7" viewBox="0 0 11 7"><path d="M1 1l4.5 4.5L10 1" fill="none" stroke="#888"/></svg>
    </div>
    <div class="field" style="left:36px;top:279px;width:504px;height:76px">Your Message</div>
    <div class="btn-dark send">SEND REQUEST
      <svg width="8" height="12" viewBox="0 0 8 12"><path d="M1 1l5 5-5 5" fill="none" stroke="#fff" stroke-width="2"/></svg>
    </div>
  </form>
  <div class="abs appt-photo" role="img" aria-label="Photo of a group therapy session with a woman, a pensive man and a counselor with a clipboard"></div>
</section>

<footer>
  <div class="abs footer-brand"><b></b>CALM SUMMIT</div>
  <div class="abs fcol" style="left:410px;top:3135px">
    <h4>SITE MAP</h4>
    <ul><li>Home</li><li>Company Information</li><li>Benefits</li><li>Press Releases</li><li>Health and Welness</li><li>Privacy Policy</li></ul>
  </div>
  <div class="abs fcol" style="left:635px;top:3135px;width:240px">
    <h4>CONTACT INFO</h4>
    <p>Address: 48 Harbor View Lane - Suite 210, Maple Bay, FL 34000<br>Phone: +1 (555) 0142-2280<br>Fax: +1 (555) 0142-2281<br>Email: info@calmsummit.example</p>
  </div>
  <div class="abs fcol" style="left:918px;top:3135px">
    <h4>FOLLOW US</h4>
    <div class="social"><i></i><i></i><i></i></div>
  </div>
  <div class="abs copyright">Copyright © 2022 Calm Summit. All Rights Reserved.</div>
</footer>

</body>
</html>
```